We need a set of stationary to compliment our new logo including letterhead (A4 & A5), envelopes, Business cards and appointment cards.

Hi Designers - our details are set out below.
Larchvale Family Medical
Shop 7, 62-64 Dunmore Avenue
TARRINGA EAST SA 5190
Phone - 08 84716392
Fax - 08 84716397
www.larchvalefm.com.au

Cheers Tess

Industry/Entity Type

Medical

Requirements
Must have
• Reflect the logo be modern and classy

```html
<!DOCTYPE html>
<html lang="en">
<head>
<meta charset="utf-8">
<title>Larchvale Family Medical – Business &amp; Appointment Cards</title>
<link rel="stylesheet" href="https://fonts.googleapis.com/css2?family=Questrial&family=Arimo:wght@400&family=Tinos:wght@700&display=swap">
<style>
  :root {
    --paper: #ffffff;
    --brand-blue: #3f86bd;
    --bright-blue: #1a90d8;
    --leaf-green: #8cc63f;
    --title-green: #2f9a3c;
    --ink: #3b3b3b;
    --rule-blue: #2a3f8f;
    --frame: #444444;
  }
  * { margin: 0; padding: 0; box-sizing: border-box; }
  html, body {
    width: 1200px; height: 349px; overflow: hidden;
    background: var(--paper);
  }
  .sheet { position: relative; width: 1200px; height: 349px; }

  .card { position: absolute; overflow: hidden; background: var(--paper); }

  .card__backdrop { position: absolute; inset: 0; }

  /* Shared brand lockup */
  .brand {
    position: absolute; text-align: center;
    font-family: "Questrial", sans-serif; color: var(--brand-blue);
  }
  .brand__dot { display: block; margin: 0 auto; border-radius: 50%; background: var(--brand-blue); }
  .brand__name { display: block; line-height: 1; letter-spacing: 0.5px; }
  .brand__sub { display: block; letter-spacing: 3px; }

  /* Business card */
  .business-card {
    left: 15px; top: 0; width: 573px; height: 340px;
    border: 1px solid var(--frame);
  }
  .business-card .card__backdrop {
    background: linear-gradient(90deg,
      #eef6fb 0%, #b9dcf1 12%, #3d9ad8 20%, #ffffff 27%,
      #ffffff 36%, #e3f0d3 44%, #b9dc95 55%, #ffffff 63%,
      #ffffff 86%, #8fc8ec 94%, #1a7fc6 100%);
  }
  .business-card .brand { left: 110px; top: 110px; width: 330px; }
  .business-card .brand__dot { width: 46px; height: 46px; margin-bottom: 18px; }
  .business-card .brand__name { font-size: 40px; }
  .business-card .brand__sub { font-size: 10px; margin-top: 5px; padding-left: 110px; }

  /* Appointment card */
  .appointment-card { left: 619px; top: 0; width: 575px; height: 338px; }
  .appointment-card .card__backdrop {
    top: 65px; bottom: 0;
    background: linear-gradient(90deg,
      #ffffff 0%, #ffffff 25%, #e6f2f9 38%, #ffffff 48%,
      #e8f3e2 62%, #ffffff 74%, #edf6ea 84%, #ffffff 94%);
  }
  .appointment-card__band-top {
    position: absolute; left: 0; top: 0; width: 100%; height: 65px;
    background: linear-gradient(90deg, #d6ead0 0%, #bfe0b5 50%, #d9ecd3 100%);
  }
  .appointment-card__title {
    position: absolute; left: 16px; top: 95px;
    font-family: "Arimo", sans-serif; font-size: 18px; font-weight: 400;
    color: var(--title-green); text-decoration: underline;
    -webkit-text-stroke: 0.4px var(--title-green);
  }
  .appointment-card .brand { left: 210px; top: 88px; width: 160px; }
  .appointment-card .brand__dot { width: 30px; height: 30px; margin-bottom: 8px; background: var(--leaf-green); }
  .appointment-card .brand__name { font-size: 19px; }
  .appointment-card .brand__sub { font-size: 6px; margin-top: 2px; padding-left: 60px; letter-spacing: 2px; }

  .practice-address {
    position: absolute; left: 387px; top: 78px; height: 48px;
    border-left: 1px solid #666; padding-left: 16px; padding-top: 12px;
    font-family: "Arimo", sans-serif; font-style: normal;
    font-size: 8.5px; line-height: 1.25; color: var(--ink);
  }

  .booking-field { position: absolute; left: 90px; display: flex; align-items: flex-end; }
  .booking-field__label {
    width: 72px;
    font-family: "Tinos", serif; font-weight: 700; font-size: 28px;
    transform: scaleX(0.82); transform-origin: left bottom;
  }
  .booking-field__line { width: 290px; height: 1px; background: var(--rule-blue); margin-bottom: 8px; }
  .booking-field--time { top: 178px; }
  .booking-field--time .booking-field__label { color: var(--title-green); }
  .booking-field--date { top: 226px; }
  .booking-field--date .booking-field__label { color: var(--bright-blue); }

  .contact-band {
    position: absolute; left: 0; top: 277px; width: 575px; height: 46px;
    background: var(--bright-blue);
    border-radius: 8px 2px 14px 4px;
    font-family: "Arimo", sans-serif; font-size: 10px; color: #ffffff;
  }
  .contact-band__web { position: absolute; left: 0; right: 0; top: 8px; text-align: center; }
  .contact-band__fax { position: absolute; left: 6px; top: 29px; }
  .contact-band__phone { position: absolute; right: 8px; top: 26px; }
</style>
</head>
<body>
<main class="sheet">

  <section class="card business-card" aria-label="Business card">
    <div class="card__backdrop" role="img" aria-label="Soft blue and green decorative background"></div>
    <div class="brand">
      <span class="brand__dot"></span>
      <span class="brand__name">LARCHVALE</span>
      <span class="brand__sub">FAMILY MEDICAL</span>
    </div>
  </section>

  <section class="card appointment-card" aria-label="Appointment card">
    <div class="card__backdrop" role="img" aria-label="Faint blue and green decorative background"></div>
    <div class="appointment-card__band-top"></div>
    <h1 class="appointment-card__title">Appointment Card</h1>
    <div class="brand">
      <span class="brand__dot"></span>
      <span class="brand__name">LARCHVALE</span>
      <span class="brand__sub">FAMILY MEDICAL</span>
    </div>
    <address class="practice-address">
      Larchvale Family Medical<br>
      Shop 7, 62-64 Dunmore Avenue<br>
      TARRINGA EAST SA 5190
    </address>
    <div class="booking-field booking-field--time">
      <span class="booking-field__label">Time</span>
      <span class="booking-field__line"></span>
    </div>
    <div class="booking-field booking-field--date">
      <span class="booking-field__label">Date</span>
      <span class="booking-field__line"></span>
    </div>
    <div class="contact-band">
      <span class="contact-band__web">www.larchvalefm.com.au</span>
      <span class="contact-band__fax">Fax - 08 84716397</span>
      <span class="contact-band__phone">Phone - 08 84716392</span>
    </div>
  </section>

</main>
</body>
</html>
```